POLITICAL CARD TO HAND OUT

A LITTLE LARGER THAN THE REGULAR BUSINESS CARD WITH THE ABOVE INFORMATION.

Industry/Entity Type

Business

Contact Information for Business Card

ELECT *DEAN HOLT* FOR JUSTICE OF THE PEACE PCT 6-EXPERIENCED LEADERSHIP- WITH MY PICTURE ON IT- PHONE 347-610-2853-MERIDIAN PRIMARY - EARLY VOTING FEB 18TH THRU FEB 28 AND ELECTION DAY IS MARCH 4TH, 2014- USE RED WHITE AND BLUE WITH SOME STARS.

Requirements
Must have
• A FIVE POINTED STAR ON EACH SIDE OF MY NAME

```html
<!DOCTYPE html>
<html lang="en">
<head>
<meta charset="utf-8">
<title>Dean Holt for Justice of the Peace</title>
<link href="https://fonts.googleapis.com/css2?family=Lato:wght@400&display=swap" rel="stylesheet">
<style>
  :root {
    --flag-red: #b70000;
    --flag-blue: #0031a2;
    --paper: #ffffff;
    --ink: #1c1c1c;
    --photo-light: #d9c7b8;
    --photo-dark: #3a2e2a;
  }
  html, body {
    margin: 0;
    padding: 0;
    overflow: hidden;
    background: var(--paper);
  }
  .card {
    position: relative;
    width: 1200px;
    height: 702px;
    overflow: hidden;
    background: var(--paper);
    font-family: "Lato", Arial, sans-serif;
  }
  .backdrop {
    position: absolute;
    inset: 0;
  }
  .backdrop .band-red { fill: var(--flag-red); }
  .backdrop .band-blue { fill: var(--flag-blue); }
  .portrait {
    position: absolute;
    left: 55px;
    top: 61px;
    width: 332px;
    height: 332px;
    border-radius: 50%;
    background: radial-gradient(circle at 50% 35%, var(--photo-light) 0%, #b89a86 40%, var(--photo-dark) 85%);
  }
  .rating {
    position: absolute;
    left: 447px;
    top: 106px;
    margin: 0;
    color: var(--paper);
    font-size: 32px;
    letter-spacing: 1px;
    line-height: 1;
  }
  .headline {
    position: absolute;
    left: 426px;
    top: 158px;
    margin: 0;
    padding: 2px 0 12px 20px;
    border-left: 3px solid var(--paper);
    color: var(--paper);
    font-weight: 400;
    font-size: 35px;
    line-height: 43px;
    letter-spacing: 0.2px;
    white-space: nowrap;
  }
  .name-star {
    font-size: 0.8em;
    vertical-align: 0.08em;
    margin: 0 2px;
  }
  .details {
    position: absolute;
    left: 142px;
    top: 532px;
    margin: 0;
    color: var(--ink);
    font-size: 34px;
    line-height: 41px;
    letter-spacing: 0.1px;
    white-space: nowrap;
  }
</style>
</head>
<body>
<div class="card">
  <svg class="backdrop" width="1200" height="702" viewBox="0 0 1200 702" aria-hidden="true">
    <polygon class="band-red" points="0,0 1200,0 1200,244 487,373 0,267"/>
    <polygon class="band-blue" points="487,373 1200,244 1200,528"/>
  </svg>

  <div class="portrait" role="img" aria-label="Portrait of the candidate in a white cowboy hat, dark suit and patterned tie"></div>

  <p class="rating" aria-label="Five stars">★★★★★</p>

  <h1 class="headline">ELECT <span class="name-star" aria-hidden="true">★</span>DEAN HOLT<span class="name-star" aria-hidden="true">★</span> FOR JUSTICE OF<br>THE PEACE PCT 6-EXPERIENCED<br>LEADERSHIP</h1>

  <p class="details">PHONE 347-610-2853-MERIDIAN PRIMARY-<br>EARLY VOTING FEB 18TH THRU FEB 28<br>ELECTION DAY IS MARCH 4TH, 2014</p>
</div>
</body>
</html>
```